Letterhead for small civil engineer company

We need bold and modern design for company letterhead in MS word. It needs to have company logo and company info. Somewhere in the upper right part of document needs to be space for "recever" and the documents starts with, example, "SUBJECT: CIVIL ENGINEER LETTERHEAD".

in the bottom part of document needs to be signature and date.

Company info: Veltrana d.o.o., Lipovac 15, Lipovac (Općina Brdarić), OIB 47396028154, www.veltrana.hr, info@veltrana.hr

Email of document sender needs to be somewhere if document, exapmle xyz@veltrana.hr

Target Market(s)

Civil engineer company and projects

Industry/Entity Type

Civil engineer

Font styles to use
Serif

Colors
F0912C
F2A743
F7CA91
FBE8D2
FDF5EE

Requirements
Must have
• Company logo and company info
Nice to have
• Moder and clean design
Should not have
• Too much details

```html
<!DOCTYPE html>
<html lang="hr">
<head>
<meta charset="utf-8">
<title>Veltrana letterhead</title>
<link rel="stylesheet" href="https://fonts.googleapis.com/css2?family=Montserrat:wght@500;600;700&family=Mulish:wght@400;500&display=swap">
<style>
  :root {
    --orange: #e98a33;
    --ink: #2b2b2b;
    --grey: #676566;
    --muted: #6e6e6e;
    --backdrop: #e0e0e0;
    --paper: #ffffff;
  }
  * { margin: 0; padding: 0; box-sizing: border-box; }
  html, body { width: 1200px; height: 1200px; overflow: hidden; }
  body { background: var(--backdrop); position: relative; font-family: "Mulish", sans-serif; color: var(--ink); }

  .letterhead {
    position: absolute; left: 216px; top: 76px;
    width: 769px; height: 1047px;
    background: var(--paper);
  }
  .brand {
    position: absolute; left: 55px; top: 73px;
    display: flex; align-items: center; gap: 8px;
  }
  .brand-square { width: 38px; height: 38px; border: 1.5px solid var(--grey); }
  .brand-name {
    font-family: "Montserrat", sans-serif; font-weight: 500;
    font-size: 33px; letter-spacing: 1px; color: var(--orange); line-height: 1;
  }
  .receiver {
    position: absolute; left: 581px; top: 88px;
    font-family: "Montserrat", sans-serif; font-weight: 600;
    font-size: 23px; letter-spacing: 2.5px; color: var(--orange);
  }
  .subject {
    position: absolute; left: 55px; top: 262px;
    font-family: "Montserrat", sans-serif; font-weight: 700;
    font-size: 19.5px; color: var(--orange);
  }
  .body-copy {
    position: absolute; left: 55px; top: 303px; width: 659px;
    font-size: 17.3px; line-height: 21.3px; text-align: justify;
  }
  .body-copy p + p { margin-top: 21.3px; }

  .sign-off { position: absolute; left: 62px; top: 767px; color: var(--muted); }
  .sign-name { font-size: 11px; font-weight: 500; }
  .sign-role { font-size: 8.5px; margin-top: 3px; }
  .signature {
    position: absolute; left: 55px; top: 800px; width: 170px; height: 75px;
    background: linear-gradient(100deg, #ffffff, #ededed 50%, #ffffff);
  }

  .contact {
    position: absolute; left: 66px; top: 969px;
    display: flex; align-items: center; font-size: 14.5px;
  }
  .contact-item { display: flex; align-items: center; gap: 8px; }
  .contact-web { width: 159px; }
  .contact-mail { width: 159px; }
  .contact-address { line-height: 15px; font-size: 14.5px; gap: 14px; }
  .contact svg { fill: none; stroke: var(--orange); stroke-width: 1.6; }

  .band-accent { position: absolute; left: 0; top: 1012px; width: 100%; height: 6px; background: var(--orange); }
  .band-base { position: absolute; left: 0; top: 1026px; width: 100%; height: 21px; background: var(--grey); }
</style>
</head>
<body>
  <main class="letterhead">
    <header class="brand">
      <div class="brand-square"></div>
      <div class="brand-name">VELTRANA</div>
    </header>
    <div class="receiver">RECEVER</div>

    <h1 class="subject">SUBJECT: CIVIL ENGINEER LETTERHEAD</h1>
    <section class="body-copy">
      <p>Lorem ipsum dolor sit amet, consectetuer adipiscing elit, sed diam nonummy nibh euismod tincidunt ut laoreet dolore magna aliquam erat volutpat. Ut wisi enim ad minim veniam, quis nostrud exerci tation ullamcorper suscipit lobortis nisl ut aliquip ex ea commodo consequat. Duis autem vel eum iriure dolor in hendrerit in vulputate velit esse molestie consequat, vel illum dolore eu feugiat nulla facilisis at vero eros et accumsan et iusto odio dignissim qui blandit praesent luptatum zzril delenit augue duis dolore te feugait nulla facilisi.</p>
      <p>Lorem ipsum dolor sit amet, cons ectetuer adipiscing elit, sed diam nonummy nibh euismod tincidunt ut laoreet dolore magna aliquam erat volutpat. Ut wisi Lorem ipsum dolor sit amet, consectetuer adipiscing elit, sed diam nonummy nibh euismod tincidunt ut laoreet dolore magna aliquam erat volutpat. Ut wisi enim ad minim veniam, quis nostrud exerci tation ullamcorper suscipit lobortis nisl ut aliquip ex ea commodo consequat. Duis autem vel eum iriure dolor in hendrerit in vulputate velit esse molestie consequat,Lorem ipsum dolor sit amet, cons ectetuer adipiscing elit, sed diam nonummy nibh euismod tincidunt ut laoreet dolore magna aliquam erat volutpat.</p>
    </section>

    <div class="sign-off">
      <div class="sign-name">Ivan Horvat</div>
      <div class="sign-role">Office Maneger</div>
    </div>
    <div class="signature" role="img" aria-label="Handwritten signature"></div>

    <footer class="contact">
      <div class="contact-item contact-web">
        <svg width="18" height="18" viewBox="0 0 18 18"><circle cx="9" cy="9" r="7.5"/><ellipse cx="9" cy="9" rx="3.3" ry="7.5"/><line x1="1.5" y1="9" x2="16.5" y2="9"/><line x1="3" y1="5" x2="15" y2="5"/><line x1="3" y1="13" x2="15" y2="13"/></svg>
        <span>www.veltrana.hr</span>
      </div>
      <div class="contact-item contact-mail">
        <svg width="20" height="15" viewBox="0 0 20 15"><rect x="1" y="1" width="18" height="13" fill="var(--orange)" stroke="none"/><polyline points="1,1 10,8 19,1" stroke="#fff"/><line x1="1" y1="14" x2="8" y2="7" stroke="#fff"/><line x1="19" y1="14" x2="12" y2="7" stroke="#fff"/></svg>
        <span>info@veltrana.hr</span>
      </div>
      <div class="contact-item contact-address">
        <svg width="14" height="22" viewBox="0 0 14 22"><path d="M7 21 C7 21 1 12 1 7.5 A6 6 0 0 1 13 7.5 C13 12 7 21 7 21 Z" stroke-width="2"/><circle cx="7" cy="7.5" r="2"/></svg>
        <span>Veltrana d.o.o., Lipovac 15,<br>Lipovac (Općina Brdarić), OIB 47396028154</span>
      </div>
    </footer>

    <div class="band-accent"></div>
    <div class="band-base"></div>
  </main>
</body>
</html>
```